Public Assistance Direct mail piece

need a full color 2 sided marketing brochure to use in direct mail campaign. finished product will be printed on 2 times. initially full color brochures to be printed in bulk. Then consumer contact info and case manager contact info will be added at a later date.
brochure will need to have 2 blank areas on front side to print address that will show thru window envelope and sales agent info on for mail campaign.
Would like to see designs that include our current color scheme and logo.
Target market. Low income poverty. Non profit service offering free assistance to help low income seniors get free assitance thru state and federal public assistance programs.
1. Sanorel - over 1 in 5 recieve help from state Sanorel. Sanorel programs for seniors and persons on Vitalcor can pay doctor copays, deductibles, and assist with medical bills.
2. Silver Bridge Program - receive Federal assistance with prescription medications, deductibles, copays, and drug plan premiums.
3. Vitalcor Thrift Program - many adults 65 and over are eligible to receive Vitalcor at no cost. The program will pay your Vitalcor Tier K premium and can even refund some previous payments.

You may be eligible to participate in one or more of these programs. All programs are based on limited income and assets.

To learn more call your local county case manager.

Knowledge is Power. Lets up help empower you.
Pay it forward. Who else do you know that is on Vitalcor that could use some help?

many graphs and illustrations are available form each government agency.

Target Market(s)

Seniors 65 plus, Vitalcor recipients

Industry/Entity Type

Marketing

Colors
0355a3
ec1f27
ffffff

Requirements
Must have
• logo, non profit, will need a government disclaimer somewhere
Nice to have
• photos of seniors saving money.

```html
<!DOCTYPE html>
<html lang="en">
<head>
<meta charset="utf-8">
<title>Elder Aid Bureau – Low Income Poverty Mailer</title>
<link href="https://fonts.googleapis.com/css2?family=Roboto:wght@400;500;700;900&family=Roboto+Condensed:wght@400;700&display=swap" rel="stylesheet">
<style>
:root{
  --navy:#0d1f4f;
  --blue:#0355a3;
  --red:#ec1f27;
  --white:#ffffff;
  --sky:#a9cdee;
  --pale:#e8eef5;
  --charcoal:#2e2f33;
  --ink:#1b1e2b;
  --stage:#b9c4d0;
}
*{box-sizing:border-box;margin:0;padding:0}
html,body{width:1200px;height:857px;overflow:hidden}
body{background:var(--stage);font-family:"Roboto",Arial,sans-serif;color:var(--ink);position:relative}
.sheet{position:absolute;top:66px;width:560px;height:725px;background:var(--white);overflow:hidden;box-shadow:0 4px 14px rgba(0,0,0,.18)}
.sheet--front{left:30px}
.sheet--back{left:610px}

/* shared brand */
.brand{position:absolute;display:flex;align-items:center;gap:8px}
.brand__dot{width:22px;height:22px;border-radius:50%;background:var(--red);flex:none}
.brand__name{font-weight:500;color:var(--navy);font-size:17px;line-height:1.05}

/* FRONT */
.front__tint{position:absolute;left:0;top:0;width:150px;height:100%;background:linear-gradient(180deg,#dfe6ef,#f3f6fa)}
.front__rule{position:absolute;left:150px;top:70px;width:6px;height:512px;background:var(--navy)}
.front .brand{left:22px;top:96px}
.title{position:absolute;right:30px;top:28px;text-align:right;font-family:"Roboto Condensed",sans-serif;font-weight:700;color:var(--navy);font-size:44px;line-height:.95;letter-spacing:.5px}
.title__accent{display:inline-block;width:90px;height:8px;background:var(--red);vertical-align:middle;margin-right:10px}
.photo-frame{position:absolute;left:175px;top:140px;width:360px;height:240px;border:10px solid var(--red)}
.photo{width:100%;height:100%;background:linear-gradient(135deg,#6f8f3c,#c9cfc2 55%,#8a6a4a)}
.lead{position:absolute;left:175px;top:394px;width:360px;font-size:11px;line-height:1.3;color:var(--navy)}
.programs{position:absolute;left:175px;top:428px;width:360px;list-style:none;font-size:11px;line-height:1.3;color:var(--navy)}
.programs li{position:relative;padding-left:12px;margin-bottom:5px}
.programs li::before{content:"";position:absolute;left:0;top:5px;width:6px;height:6px;background:var(--red)}
.eligible{position:absolute;left:175px;top:594px;width:365px;font-weight:700;font-size:12px;line-height:1.35;color:var(--ink)}
.callout-band{position:absolute;left:0;top:640px;width:100%;height:30px;background:var(--charcoal);color:var(--white);font-size:13px;display:flex;align-items:center;justify-content:center}
.site{position:absolute;left:0;width:100%;text-align:center;font-weight:700;letter-spacing:3px;color:var(--navy);font-size:14px}
.front .site{top:684px}
.front__foot{position:absolute;left:0;bottom:0;width:100%;height:10px;background:var(--navy)}

/* BACK */
.headline{position:absolute;left:24px;top:18px;font-weight:900;color:var(--red);font-size:23px}
.subline{position:absolute;left:24px;top:50px;font-size:11px;color:var(--ink)}
.fact-band{position:absolute;left:0;top:72px;width:100%;height:54px;background:var(--charcoal);color:var(--white);text-align:center;padding-top:8px}
.fact-band__main{font-weight:700;font-size:14px}
.fact-band__sub{font-size:10px;margin-top:3px}
.donuts{position:absolute;left:16px;top:140px;width:528px;display:flex;justify-content:space-between}
.donut{width:124px;text-align:center}
.donut svg{display:block;margin:0 auto}
.donut__label{font-size:9px;font-weight:700;fill:var(--navy)}
.donut__note{font-size:8.5px;line-height:1.25;margin-top:4px;color:var(--ink)}
.paid-panel{position:absolute;left:210px;top:268px;width:350px;height:150px;background:var(--charcoal);color:var(--white);padding:14px 10px 0 108px}
.paid-panel__title{font-weight:700;font-size:19px}
.paid-row{display:flex;gap:12px;margin-top:10px}
.paid-stat{display:flex;align-items:center;gap:5px;white-space:nowrap}
.paid-stat__frac{font-weight:700;font-size:34px;line-height:1}
.paid-stat__text{font-size:10.5px;line-height:1.2}
.booster{position:absolute;left:20px;top:292px;width:280px;height:180px;background:var(--white);border:4px solid var(--charcoal);padding:8px 10px}
.booster__title{font-weight:900;color:var(--navy);font-size:15px}
.booster__sub{font-size:9px;margin:2px 0 6px}
.booster__art{width:100%;height:110px;background:linear-gradient(180deg,#9fcbe9,#f1d28a)}
.map-title{position:absolute;left:22px;top:486px;font-weight:700;color:var(--red);font-size:12px}
.map-sub{position:absolute;left:22px;top:502px;font-size:9.5px;color:var(--navy)}
.map{position:absolute;left:22px;top:520px;width:250px;height:125px;background:linear-gradient(135deg,#1c3a7a,#6f97cf 60%,#c6dcf1)}
.legend{position:absolute;left:290px;top:520px;list-style:none;font-size:12px;color:var(--navy)}
.legend li{display:flex;align-items:center;gap:6px;margin-bottom:5px}
.legend i{width:12px;height:12px;display:block}
.contact{position:absolute;left:395px;top:440px;width:165px}
.contact .brand{position:static;margin-bottom:10px}
.contact .brand__name{font-size:13px}
.contact__box{background:var(--navy);color:var(--white);font-size:10px;line-height:1.5;padding:8px 10px}
.map-note{position:absolute;left:22px;top:652px;width:516px;font-size:8px;line-height:1.3;color:var(--navy)}
.back__foot{position:absolute;left:0;bottom:0;width:100%;height:38px;background:var(--navy)}
.back .site{bottom:10px;color:var(--white)}
</style>
</head>
<body>

<section class="sheet sheet--front front">
  <div class="front__tint"></div>
  <div class="front__rule"></div>
  <div class="brand"><span class="brand__dot"></span><span class="brand__name">Elder Aid<br>Bureau</span></div>
  <h1 class="title">LOW INCOME<br><span class="title__accent"></span>POVERTY</h1>
  <div class="photo-frame"><div class="photo" role="img" aria-label="Smiling senior woman counting money from her wallet outdoors"></div></div>
  <p class="lead">Non profit service offering free assistance to help low income seniors get free assitance thru state and federal public assistance programs.</p>
  <ul class="programs">
    <li>Sanorel - over 1 in 5 recieve help from state Sanorel. Sanorel programs for seniors and persons on Vitalcor can pay doctor copays, deductibles, and assist with medical bills.</li>
    <li>Silver Bridge Program - receive Federal assistance with prescription medications, deductibles, copays, and drug plan premiums.</li>
    <li>Vitalcor Thrift Program - many adults 65 and over are eligible to receive Vitalcor at no cost. The program will pay your Vitalcor Tier K premium and can even refund some previous payments.</li>
  </ul>
  <p class="eligible">You may be eligible to participate in one or more of these programs. All programs are based on limited income and assets.</p>
  <div class="callout-band">To learn more call your local county case manager.</div>
  <p class="site">www.elderaidbureau.org</p>
  <div class="front__foot"></div>
</section>

<section class="sheet sheet--back back">
  <h2 class="headline">Knowledge is Power. Lets up help empower you.</h2>
  <p class="subline">Pay it forward. Who else do you know that is on Vitalcor that could use some help?</p>
  <div class="fact-band">
    <p class="fact-band__main">Sanorel was created in 1965 as a program for the poor.</p>
    <p class="fact-band__sub">Today, it helps 74 million people — more than 1 of every 5 people in the U.S. You or someone you know likely benefits.</p>
  </div>

  <div class="donuts">
    <figure class="donut">
      <svg width="90" height="90" viewBox="0 0 90 90"><circle cx="45" cy="45" r="34" fill="none" stroke="var(--sky)" stroke-width="12"/><circle cx="45" cy="45" r="34" fill="none" stroke="var(--navy)" stroke-width="12" stroke-dasharray="96.1 213.6" transform="rotate(-90 45 45)"/><text x="45" y="48" text-anchor="middle" class="donut__label">Births</text></svg>
      <figcaption class="donut__note">45 percent of all births are paid for by Sanorel</figcaption>
    </figure>
    <figure class="donut">
      <svg width="90" height="90" viewBox="0 0 90 90"><circle cx="45" cy="45" r="34" fill="none" stroke="var(--sky)" stroke-width="12"/><circle cx="45" cy="45" r="34" fill="none" stroke="var(--navy)" stroke-width="12" stroke-dasharray="83.3 213.6" transform="rotate(-90 45 45)"/><text x="45" y="48" text-anchor="middle" class="donut__label">Children</text></svg>
      <figcaption class="donut__note">39 percent of children are covered by Sanorel</figcaption>
    </figure>
    <figure class="donut">
      <svg width="90" height="90" viewBox="0 0 90 90"><circle cx="45" cy="45" r="34" fill="none" stroke="var(--sky)" stroke-width="12"/><circle cx="45" cy="45" r="34" fill="none" stroke="var(--navy)" stroke-width="12" stroke-dasharray="87.6 213.6" transform="rotate(-90 45 45)"/><text x="45" y="44" text-anchor="middle" class="donut__label">Adults</text><text x="45" y="55" text-anchor="middle" class="donut__label">With HIV</text></svg>
      <figcaption class="donut__note">41 percent of adults with HIV ages 18-64 are covered by Sanorel</figcaption>
    </figure>
    <figure class="donut">
      <svg width="90" height="90" viewBox="0 0 90 90"><circle cx="45" cy="45" r="34" fill="none" stroke="var(--sky)" stroke-width="12"/><circle cx="45" cy="45" r="34" fill="none" stroke="var(--navy)" stroke-width="12" stroke-dasharray="132.4 213.6" transform="rotate(-90 45 45)"/><text x="45" y="38" text-anchor="middle" class="donut__label">Nursing</text><text x="45" y="49" text-anchor="middle" class="donut__label">home</text><text x="45" y="60" text-anchor="middle" class="donut__label">residents</text></svg>
      <figcaption class="donut__note">62 percent of nursing home residents are covered by Sanorel</figcaption>
    </figure>
  </div>

  <div class="paid-panel">
    <p class="paid-panel__title">SANOREL PAID FOR</p>
    <div class="paid-row">
      <div class="paid-stat"><span class="paid-stat__frac">1/4</span><span class="paid-stat__text">of all<br>mental<br>health<br>services</span></div>
      <div class="paid-stat"><span class="paid-stat__frac">1/5</span><span class="paid-stat__text">of all<br>substance<br>abuse<br>treatment</span></div>
    </div>
  </div>

  <div class="booster">
    <p class="booster__title">BIG SCHOOL BOOSTER</p>
    <p class="booster__sub">Sanorel paid for nearly $4 billion in school based health care services in 2015.</p>
    <div class="booster__art" role="img" aria-label="Classroom illustration with desks and a chalkboard reading $4 Billion"></div>
  </div>

  <p class="map-title">The Sanorel Landscape: State-By-State Coverage</p>
  <p class="map-sub">Percent of Population Covered By Sanorel/YCF, 2016</p>
  <div class="map" role="img" aria-label="Map of U.S. states shaded by percent of population covered"></div>
  <ul class="legend">
    <li><i style="background:#c6dcf1"></i>10-13%</li>
    <li><i style="background:#8fb4e0"></i>14-17%</li>
    <li><i style="background:#5a86c4"></i>18-21%</li>
    <li><i style="background:#2c5597"></i>22-27%</li>
    <li><i style="background:#0d1f4f"></i>28-31%</li>
  </ul>

  <div class="contact">
    <div class="brand"><span class="brand__dot"></span><span class="brand__name">Elder Aid Bureau</span></div>
    <div class="contact__box">877-555-0142<br>P.O. Box 4410<br>Pine Hollow, SC 29000<br>hello@elderaidbureau.org</div>
  </div>

  <p class="map-note">Note: Includes those covered by Sanorel, the Youth Care Fund (YCF) and those who have both Sanorel and another type of coverage, such as dual eligibles who are also covered by Vitalcor.</p>
  <div class="back__foot"></div>
  <p class="site">www.elderaidbureau.org</p>
</section>

</body>
</html>
```